Intenational Rhythmic Gymnastics Frostvale Trophy

We need a poster for our new annual international rhythmic gymnastics competition "Frostvale Trophy". Dates are December 21 -23, 2019.Picture we would like to use is attached.We would like to see holidays colors in the poster.It should have words "international rhythmic gymnastics", Name of the competition "Frostvale Trophy" and dates.Also we would like for it to say somewhere that it is in Los Angeles, California, USAIt should have information about our club on the bottom of the poster like on the file attached (hosted by Tamrin Gymnastics with logo and address and website info)We also need a flyer that ties into the poster in look and colors with empty space below so we can add directives.We would like end product to be in file format that we can edit next year when the dates change.

Target Market(s)

Rhythmic Gymnastics Clubs

Industry/Entity Type

Gym

Colors

Designer to choose colors to be used in the design.

Requirements
Must have
• Picture we uploaded and all info we requested.
• Bright holiday colors

```html
<!DOCTYPE html>
<html lang="en">
<head>
<meta charset="utf-8">
<title>Frostvale Trophy 2019 – Poster Variants</title>
<link rel="stylesheet" href="https://fonts.googleapis.com/css2?family=Montserrat:wght@300;400;700;900&display=swap">
<style>
  :root {
    --stage-grey: #dcdcdc;
    --stage-white: #ffffff;
    --stage-light: #e9e9e9;
    --royal-blue: #2148a0;
    --ocean-blue: #1a6aa8;
    --festive-red: #d12a3a;
    --tangerine: #f2821e;
    --holly-green: #6abf46;
    --title-white: #ececec;
    --ink-white: #ffffff;
    --band-shade: rgba(10, 20, 45, 0.35);
  }
  * { box-sizing: border-box; margin: 0; padding: 0; }
  html, body { width: 1200px; height: 3600px; overflow: hidden; }
  body { font-family: "Montserrat", sans-serif; color: var(--ink-white); }

  .stage { position: relative; width: 1200px; height: 1200px; }
  .stage--grey { background: var(--stage-grey); }
  .stage--white { background: var(--stage-white); }
  .stage--light { background: var(--stage-light); height: 1200px; }

  .poster {
    position: absolute; left: 293px; top: 166px;
    width: 614px; height: 866px; overflow: hidden;
    background: var(--poster-bg);
  }
  .poster--blue { --poster-bg: radial-gradient(ellipse at 50% 40%, #2a56b4 0%, var(--royal-blue) 60%, #183a88 100%); --accent: var(--tangerine); }
  .poster--ocean { --poster-bg: radial-gradient(ellipse at 50% 40%, #2479b8 0%, var(--ocean-blue) 60%, #155a94 100%); --accent: var(--tangerine); }
  .poster--red { --poster-bg: radial-gradient(ellipse at 50% 40%, #e0364a 0%, var(--festive-red) 60%, #b61f30 100%); --accent: var(--holly-green); }

  .accent-block { position: absolute; left: 112px; width: 80px; background: var(--accent); }
  .accent-block--top { top: 0; height: 64px; }
  .accent-block--bottom { top: 800px; height: 66px; }

  .event-kicker {
    position: absolute; left: 110px; top: 84px; width: 393px;
    font-weight: 400; font-size: 17.5px; letter-spacing: 0.2px; white-space: nowrap;
  }

  .athlete-photo {
    position: absolute; left: 130px; top: 300px; width: 400px; height: 290px;
    border-radius: 50% 50% 12% 12%;
    background: radial-gradient(ellipse at 45% 40%, rgba(190,140,110,0.75) 0%, rgba(110,70,120,0.55) 45%, rgba(60,40,70,0) 75%);
  }

  .event-title { position: absolute; left: 110px; top: 105px; width: 393px; height: 340px; }
  .event-title text { font-family: "Montserrat", sans-serif; font-weight: 900; }

  .event-dates {
    position: absolute; left: 0; right: 0; top: 606px; text-align: center;
    font-weight: 300; font-size: 43px; letter-spacing: 0.5px;
  }
  .event-dates sup { font-size: 24px; vertical-align: 18px; }
  .event-venue {
    position: absolute; left: 0; right: 0; top: 673px; text-align: center;
    font-size: 17px; font-weight: 400;
  }
  .event-venue strong { font-weight: 700; }

  .host-band {
    position: absolute; left: 0; top: 729px; width: 614px; height: 52px;
    background: var(--band-shade);
  }
  .host-tag {
    position: absolute; left: 112px; top: 4px; width: 17px; height: 44px;
    background: var(--ink-white); color: #333;
    font-size: 7px; font-weight: 700; writing-mode: vertical-rl; transform: rotate(180deg);
    display: flex; align-items: center; justify-content: center; letter-spacing: 0.5px;
  }
  .host-name {
    position: absolute; left: 162px; top: 16px;
    font-size: 15px; font-weight: 400; white-space: nowrap;
  }
  .host-name::after {
    content: ""; display: inline-block; width: 9px; height: 9px; margin-left: 8px;
    border-radius: 50%; background: var(--ink-white);
  }
  .host-contact { position: absolute; left: 331px; top: 11px; font-size: 8.5px; line-height: 16px; }
  .host-contact li { list-style: none; display: flex; align-items: center; gap: 5px; white-space: nowrap; }
  .host-contact svg { width: 8px; height: 8px; fill: var(--ink-white); }
</style>
</head>
<body>

<svg width="0" height="0" style="position:absolute">
  <defs>
    <linearGradient id="title-orange-wash" x1="0" y1="0" x2="1" y2="0.3">
      <stop offset="0" stop-color="#ececec"/>
      <stop offset="0.45" stop-color="#ececec"/>
      <stop offset="0.7" stop-color="#f7a559"/>
      <stop offset="1" stop-color="#f2821e"/>
    </linearGradient>
  </defs>
</svg>

<section class="stage stage--grey">
  <article class="poster poster--blue">
    <div class="accent-block accent-block--top"></div>
    <p class="event-kicker">INTERNATIONAL RHYTHMIC GYMNASTICS</p>
    <svg class="event-title" viewBox="0 0 393 340">
      <text x="0" y="72" textLength="393" lengthAdjust="spacingAndGlyphs" font-size="90" fill="#ececec">FROSTVALE</text>
      <text x="0" y="208" textLength="393" lengthAdjust="spacingAndGlyphs" font-size="150" fill="url(#title-orange-wash)">TROPHY</text>
      <text x="0" y="336" textLength="393" lengthAdjust="spacingAndGlyphs" font-size="150" fill="url(#title-orange-wash)">2019</text>
    </svg>
    <div class="athlete-photo" role="img" aria-label="Rhythmic gymnast in a jewelled leotard in a deep lunge, with a swirling ribbon"></div>
    <p class="event-dates">December 21-23<sup>rd</sup></p>
    <p class="event-venue">at <strong>Los Angeles, California</strong></p>
    <div class="host-band">
      <span class="host-tag">HOST BY</span>
      <span class="host-name">Tamrin Gymnastics</span>
      <ul class="host-contact">
        <li><svg viewBox="0 0 10 10"><path d="M5 0a3.5 3.5 0 0 0-3.5 3.5C1.5 6 5 10 5 10s3.5-4 3.5-6.5A3.5 3.5 0 0 0 5 0zm0 5a1.4 1.4 0 1 1 0-2.8A1.4 1.4 0 0 1 5 5z"/></svg>4820 Alder Crest Ave, #212 Northvale, CA 91402</li>
        <li><svg viewBox="0 0 10 10"><circle cx="5" cy="5" r="4.5"/></svg>www.tamringymnastics.com</li>
      </ul>
    </div>
    <div class="accent-block accent-block--bottom"></div>
  </article>
</section>

<section class="stage stage--white">
  <article class="poster poster--ocean">
    <div class="accent-block accent-block--top"></div>
    <p class="event-kicker">INTERNATIONAL RHYTHMIC GYMNASTICS</p>
    <svg class="event-title" viewBox="0 0 393 340">
      <text x="0" y="72" textLength="393" lengthAdjust="spacingAndGlyphs" font-size="90" fill="#ececec">FROSTVALE</text>
      <text x="0" y="208" textLength="393" lengthAdjust="spacingAndGlyphs" font-size="150" fill="#ececec">TROPHY</text>
      <text x="0" y="336" textLength="393" lengthAdjust="spacingAndGlyphs" font-size="150" fill="#ececec">2019</text>
    </svg>
    <div class="athlete-photo" role="img" aria-label="Rhythmic gymnast in a jewelled leotard in a deep lunge, with a swirling ribbon"></div>
    <p class="event-dates">December 21-23<sup>rd</sup></p>
    <p class="event-venue">at <strong>Los Angeles, California</strong></p>
    <div class="host-band">
      <span class="host-tag">HOST BY</span>
      <span class="host-name">Tamrin Gymnastics</span>
      <ul class="host-contact">
        <li><svg viewBox="0 0 10 10"><path d="M5 0a3.5 3.5 0 0 0-3.5 3.5C1.5 6 5 10 5 10s3.5-4 3.5-6.5A3.5 3.5 0 0 0 5 0zm0 5a1.4 1.4 0 1 1 0-2.8A1.4 1.4 0 0 1 5 5z"/></svg>4820 Alder Crest Ave, #212 Northvale, CA 91402</li>
        <li><svg viewBox="0 0 10 10"><circle cx="5" cy="5" r="4.5"/></svg>www.tamringymnastics.com</li>
      </ul>
    </div>
    <div class="accent-block accent-block--bottom"></div>
  </article>
</section>

<section class="stage stage--light">
  <article class="poster poster--red">
    <div class="accent-block accent-block--top"></div>
    <p class="event-kicker">INTERNATIONAL RHYTHMIC GYMNASTICS</p>
    <svg class="event-title" viewBox="0 0 393 340">
      <text x="0" y="72" textLength="393" lengthAdjust="spacingAndGlyphs" font-size="90" fill="#ececec">FROSTVALE</text>
      <text x="0" y="208" textLength="393" lengthAdjust="spacingAndGlyphs" font-size="150" fill="#ececec">TROPHY</text>
      <text x="0" y="336" textLength="393" lengthAdjust="spacingAndGlyphs" font-size="150" fill="#ececec">2019</text>
    </svg>
    <div class="athlete-photo" role="img" aria-label="Rhythmic gymnast in a jewelled leotard in a deep lunge, with a swirling ribbon"></div>
    <p class="event-dates">December 21-23<sup>rd</sup></p>
    <p class="event-venue">at <strong>Los Angeles, California</strong></p>
    <div class="host-band">
      <span class="host-tag">HOST BY</span>
      <span class="host-name">Tamrin Gymnastics</span>
      <ul class="host-contact">
        <li><svg viewBox="0 0 10 10"><path d="M5 0a3.5 3.5 0 0 0-3.5 3.5C1.5 6 5 10 5 10s3.5-4 3.5-6.5A3.5 3.5 0 0 0 5 0zm0 5a1.4 1.4 0 1 1 0-2.8A1.4 1.4 0 0 1 5 5z"/></svg>4820 Alder Crest Ave, #212 Northvale, CA 91402</li>
        <li><svg viewBox="0 0 10 10"><circle cx="5" cy="5" r="4.5"/></svg>www.tamringymnastics.com</li>
      </ul>
    </div>
    <div class="accent-block accent-block--bottom"></div>
  </article>
</section>

</body>
</html>
```